Velvet Parlour Site Make Over

I would like to get a site makeover for www.velvetparlour.example. The two main pages are the products pages eg: http://www.velvetparlour.example.au/products/marovine.html

and the home page. Please focus more on the products page as it is 10x more important than the home page.

The width of the pages should be 990px.
Updates

Target Market(s)

WOmen aged 18-35

Industry/Entity Type

Club

Requirements
Must have
• must be "pretty"

```html
<!DOCTYPE html>
<html lang="en">
<head>
<meta charset="utf-8">
<title>Velvet Parlour – Home</title>
<link href="https://fonts.googleapis.com/css2?family=Playball&display=swap" rel="stylesheet">
<style>
  :root {
    --magenta: #b51a55;
    --plum: #5e2a8e;
    --lavender: #a98bd8;
    --rose: #f0a5b5;
    --orchid: #dea3d6;
    --blush: #f0cdee;
    --headline: #c23a8e;
    --headline-soft: #f29fb7;
    --white: #ffffff;
    --ink: #1a1a1a;
  }
  * { box-sizing: border-box; margin: 0; padding: 0; }
  html, body { width: 1200px; height: 728px; overflow: hidden; background: var(--white); }
  body { font-family: "Playball", cursive; color: var(--ink); }
  .canvas { position: relative; width: 1200px; height: 728px; overflow: hidden; }

  .round { position: absolute; border-radius: 50%; display: flex; flex-direction: column;
           align-items: center; justify-content: center; text-align: center; }

  .brand { position: absolute; left: 37px; top: 82px; display: flex; align-items: center; gap: 12px; }
  .brand-dot { width: 30px; height: 30px; border-radius: 50%; background: var(--magenta); }
  .brand-name { font-size: 40px; line-height: 1; color: var(--magenta); }

  .utility { position: absolute; top: 12px; height: 30px; color: var(--white); font-size: 20px;
             display: flex; align-items: center; justify-content: center; text-decoration: none; }
  .utility-faq { left: 550px; width: 126px; background: var(--magenta); }
  .utility-login { left: 696px; width: 126px; background: var(--plum); }
  .utility-search { left: 840px; width: 126px; background: var(--magenta); }
  .search-field { position: absolute; left: 970px; top: 12px; width: 127px; height: 30px;
                  border: 2px solid var(--ink); background: var(--white); }

  .nav-item { top: 77px; width: 100px; height: 100px; color: var(--white); font-size: 23px; text-decoration: none; }
  .nav-plum { background: var(--plum); }
  .nav-magenta { background: var(--magenta); }

  .category { position: absolute; left: 36px; width: 389px; height: 89px; color: var(--white);
              display: flex; align-items: center; justify-content: space-between; padding: 0 16px 0 52px; }
  .category-arrows { font-family: Arial, sans-serif; font-size: 15px; letter-spacing: 2px; }
  .category-label { font-size: 30px; }
  .category-makeup { top: 294px; background: var(--lavender); }
  .category-fragrance { top: 383px; background: var(--rose); }
  .category-skincare { top: 472px; background: var(--orchid); }

  .hero-photo { position: absolute; left: 432px; top: 195px; width: 390px; height: 363px;
                background: linear-gradient(160deg, #f4efed 0%, #d9c3b8 45%, #9a9797 100%); }

  .headline { position: absolute; right: 75px; top: 230px; text-align: right; font-size: 27px;
              line-height: 1.08; font-weight: 400; }
  .headline-lead { color: var(--headline); }
  .headline-sub { color: var(--headline-soft); }

  .start-now { left: 976px; top: 319px; width: 140px; height: 140px; background: var(--blush);
               color: var(--magenta); font-size: 24px; text-decoration: none; }

  .slogan { position: absolute; right: 78px; top: 462px; color: var(--headline-soft); font-size: 25px; }

  .top-ten { top: 570px; width: 166px; height: 150px; font-size: 27px; line-height: 1.05; color: var(--ink); }
  .top-makeup { left: 30px; background: var(--lavender); }
  .top-fragrance { left: 397px; background: var(--rose); }
  .top-skincare { left: 775px; background: var(--blush); }

  .top-list { position: absolute; top: 590px; list-style: none; font-size: 11.5px; line-height: 16.5px; }
  .top-list li::before { content: "- "; }
  .list-makeup { left: 206px; }
  .list-fragrance { left: 574px; }
  .list-skincare { left: 958px; }
</style>
</head>
<body>
<div class="canvas">

  <header>
    <div class="brand">
      <span class="brand-dot"></span>
      <span class="brand-name">velvet parlour</span>
    </div>

    <a class="utility utility-faq" href="#">faq</a>
    <a class="utility utility-login" href="#">login</a>
    <a class="utility utility-search" href="#">search</a>
    <div class="search-field" aria-label="Search field"></div>

    <nav>
      <a class="round nav-item nav-plum" style="left:388px" href="#">haircare</a>
      <a class="round nav-item nav-magenta" style="left:508px" href="#">skincare</a>
      <a class="round nav-item nav-plum" style="left:628px" href="#">fragrance</a>
      <a class="round nav-item nav-magenta" style="left:751px" href="#">make up</a>
      <a class="round nav-item nav-plum" style="left:875px" href="#">blog</a>
      <a class="round nav-item nav-magenta" style="left:1000px" href="#">forum</a>
    </nav>
  </header>

  <main>
    <div class="category category-makeup"><span class="category-arrows">&gt;&gt;&gt;</span><span class="category-label">Make up brands</span></div>
    <div class="category category-fragrance"><span class="category-arrows">&gt;&gt;&gt;</span><span class="category-label">Designer fragrances</span></div>
    <div class="category category-skincare"><span class="category-arrows">&gt;&gt;&gt;</span><span class="category-label">Skincare brands</span></div>

    <div class="hero-photo" role="img" aria-label="Photo of a smiling young woman resting her chin on her hands"></div>

    <h1 class="headline">
      <span class="headline-lead">Join the Velvet Parlour today!</span><br>
      <span class="headline-sub">Find the right products to be your</span><br>
      <span class="headline-sub">most beautiful self</span>
    </h1>

    <a class="round start-now" href="#">Start Now</a>

    <p class="slogan">Beauty lovers, come find your glow!</p>

    <div class="round top-ten top-makeup">Top 10<br>Make up</div>
    <ul class="top-list list-makeup">
      <li>Lunelle No4 Eyeshadow</li>
      <li>Marisol 100% natural lip balm</li>
      <li>Orvane 100% oil free foundation</li>
      <li>Celeste Rhee long wear liquid base</li>
      <li>Tavira Blush – No. 7 Soft Coral</li>
      <li>Nerissa cooling tinted primer</li>
      <li>Odalie glow stick highlighter</li>
    </ul>

    <div class="round top-ten top-fragrance">Top 10<br>Fragrance</div>
    <ul class="top-list list-fragrance">
      <li>Lunelle No4 Eyeshadow</li>
      <li>Marisol 100% natural lip balm</li>
      <li>Orvane 100% oil free foundation</li>
      <li>Celeste Rhee long wear liquid base</li>
      <li>Tavira Blush – No. 7 Soft Coral</li>
      <li>Nerissa cooling tinted primer</li>
      <li>Odalie glow stick highlighter</li>
    </ul>

    <div class="round top-ten top-skincare">Top 10<br>Skincare</div>
    <ul class="top-list list-skincare">
      <li>Lunelle No4 Eyeshadow</li>
      <li>Marisol 100% natural lip balm</li>
      <li>Orvane 100% oil free foundation</li>
      <li>Celeste Rhee long wear liquid base</li>
      <li>Tavira Blush – No. 7 Soft Coral</li>
      <li>Nerissa cooling tinted primer</li>
      <li>Odalie glow stick highlighter</li>
    </ul>
  </main>

</div>
</body>
</html>
```